Fun relaxed Travel Photography Business Card*

Require a fun, funky and quirky but rememberable business card for a travel photographer

Industry/Entity Type

Photographer

Contact Information for Business Card

Front Card

(my name) Tavo M.

Travel Photographer ( small under travel photographer) “self-proclaimed”

(website logo) wanderingtavo.example

(Snapfeed logo) @wandering_with_tavo

(Snapfeed logo) @wandering_with_tavo_2.0 (backup for when Snapfeed puts Tavo on timeout for bad behaviour)

Tel: N/A (removing the potential awkwardness of me not replying)

Email: (see above)

Back Card

Offending people since 1986

(Bottom right corner) “p.s. travelling made me fatTER”

Font styles to use
Serif

Colors

Designer to choose colors to be used in the design.

Requirements
Must have
• a camera
• a similar cartoon version of me as the "logo" see attached files, try to make as similar as possible

```html
<!DOCTYPE html>
<html lang="en">
<head>
<meta charset="utf-8">
<title>Tavo M. — Travel Photographer Business Card</title>
<link rel="stylesheet" href="https://fonts.googleapis.com/css2?family=Yellowtail&family=Kaushan+Script&family=Fira+Sans+Condensed:wght@600&family=Raleway:wght@300;400;700&family=Open+Sans:wght@600&display=swap">
<style>
  :root {
    --backdrop: #dcdcdc;
    --navy: #0d2f5e;
    --navy-deep: #0a2446;
    --white: #ffffff;
    --soft-white: #e6ecf5;
    --sky: #2a9be0;
    --sky-light: #8fd0f5;
    --plane: #c9d2de;
  }
  * { margin: 0; padding: 0; box-sizing: border-box; }
  html, body { width: 1200px; height: 1083px; overflow: hidden; }
  body {
    background: var(--backdrop);
    position: relative;
    font-family: "Raleway", sans-serif;
    color: var(--white);
  }
  .card {
    position: absolute;
    left: 180px;
    width: 840px;
    height: 480px;
    background: var(--navy);
    overflow: hidden;
    box-shadow: 0 6px 18px rgba(0,0,0,.18);
  }
  .card--back { top: 40px; }
  .card--front { top: 563px; }

  /* Back card */
  .back__band {
    position: absolute; left: 0; right: 0; bottom: 0; height: 96px;
    background: var(--navy-deep);
  }
  .back__name {
    position: absolute; left: 190px; top: 36px;
    font-family: "Yellowtail", cursive; font-weight: 400; font-size: 72px; line-height: 1;
  }
  .back__rule {
    position: absolute; left: 150px; top: 118px; width: 150px; height: 3px;
    background: var(--white); border-radius: 2px;
  }
  .back__tagline {
    position: absolute; left: 70px; top: 124px;
    font-family: "Kaushan Script", cursive; font-size: 50px; line-height: 1.15;
  }
  .back__tagline span { display: block; padding-left: 30px; }
  .back__ps {
    position: absolute; left: 60px; bottom: 32px;
    font-family: "Open Sans", sans-serif; font-weight: 600; font-size: 26px;
    display: flex; align-items: center; gap: 12px;
  }
  .back__ps::before {
    content: ""; width: 6px; height: 6px; border-radius: 50%; background: var(--soft-white);
  }
  .back__camera {
    position: absolute; right: 0; top: 150px; width: 360px; height: 234px;
  }

  /* Front card */
  .front__panel {
    position: absolute; right: 0; top: 0; bottom: 0; width: 230px;
    background: var(--navy-deep);
  }
  .front__name {
    position: absolute; left: 120px; top: 22px;
    font-family: "Yellowtail", cursive; font-weight: 400; font-size: 92px; line-height: 1;
  }
  .front__title {
    position: absolute; left: 64px; top: 124px;
    font-family: "Fira Sans Condensed", sans-serif; font-weight: 600;
    font-size: 30px; letter-spacing: .5px; text-transform: uppercase;
  }
  .front__subtitle {
    position: absolute; left: 90px; top: 160px;
    font-weight: 300; font-size: 24px; letter-spacing: 1px;
  }
  .contacts { position: absolute; left: 44px; top: 214px; list-style: none; }
  .contacts__item {
    display: flex; align-items: center; gap: 12px;
    font-size: 25px; font-weight: 400; line-height: 1.45;
  }
  .contacts__mark {
    width: 18px; height: 18px; border-radius: 50%; background: var(--sky-light); flex: none;
  }
  .contacts__note {
    padding-left: 30px; font-size: 17px; font-weight: 300; line-height: 1.3; color: var(--soft-white);
  }
  .front__avatar {
    position: absolute; left: 400px; top: 215px; width: 200px; height: 200px;
  }
  .front__plane {
    position: absolute; right: 60px; top: 36px; width: 110px; height: 110px;
  }
  .reach {
    position: absolute; right: 30px; top: 200px; width: 170px; text-align: right;
  }
  .reach__label { font-size: 16px; letter-spacing: 5px; font-weight: 400; }
  .reach__value { font-size: 22px; font-weight: 700; line-height: 1.2; }
  .reach__note { font-size: 16px; font-weight: 300; line-height: 1.25; margin-bottom: 18px; }
</style>
</head>
<body>

  <section class="card card--back" aria-label="Business card, back">
    <div class="back__band"></div>
    <h2 class="back__name">Tavo M.</h2>
    <div class="back__rule"></div>
    <p class="back__tagline">Offending people <span>since 1986</span></p>
    <svg class="back__camera" viewBox="0 0 360 234" role="img" aria-label="Large cartoon camera illustration">
      <defs>
        <linearGradient id="camera-fill" x1="0" y1="0" x2="1" y2="1">
          <stop offset="0" stop-color="#d8d8d8"/>
          <stop offset="1" stop-color="#8e8e8e"/>
        </linearGradient>
      </defs>
      <rect x="0" y="0" width="400" height="260" rx="30" fill="url(#camera-fill)"/>
    </svg>
    <p class="back__ps">PS. traveling made me fat(TER)</p>
  </section>

  <section class="card card--front" aria-label="Business card, front">
    <div class="front__panel"></div>
    <h1 class="front__name">Tavo M.</h1>
    <p class="front__title">Travel Photographer</p>
    <p class="front__subtitle">.self-proclaimed.</p>
    <ul class="contacts">
      <li class="contacts__item"><span class="contacts__mark"></span>wanderingtavo.example</li>
      <li class="contacts__item"><span class="contacts__mark"></span>@wandering_with_tavo</li>
      <li class="contacts__item"><span class="contacts__mark"></span>@wandering_with_tavo_2.0</li>
      <li class="contacts__note">(backup for when Snapfeed puts<br>Tavo on timeout for bad behavior)</li>
    </ul>
    <svg class="front__avatar" viewBox="0 0 200 200" role="img" aria-label="Cartoon portrait of the photographer with sunglasses and a camera">
      <defs>
        <linearGradient id="avatar-sky" x1="0" y1="0" x2="0" y2="1">
          <stop offset="0" stop-color="#8fd0f5"/>
          <stop offset="1" stop-color="#2a9be0"/>
        </linearGradient>
      </defs>
      <circle cx="100" cy="100" r="94" fill="url(#avatar-sky)" stroke="#ffffff" stroke-width="7"/>
    </svg>
    <svg class="front__plane" viewBox="0 0 110 110" role="img" aria-label="Airplane illustration">
      <circle cx="55" cy="55" r="48" fill="var(--plane)" opacity=".35"/>
    </svg>
    <div class="reach">
      <p class="reach__label">PHONE:</p>
      <p class="reach__value">N/A</p>
      <p class="reach__note">(removing the potential awkwardness of me not replying)</p>
      <p class="reach__label">MAIL:</p>
      <p class="reach__value">(see above)</p>
    </div>
  </section>

</body>
</html>
```